Business Card Design

We are a project managment company specializing in Interior fitout
PVH is for Commercial, Domestic, Industial - we provide managment to these industries and see the projects through design to contruction
Would like an area on the back of the card where peoplr can write notes
Thinking laser lines and architectural finishes
Colour theme at the moment is light grey and red although im open to any colour/design scheme

Industry/Entity Type

Business

Contact Information for Business Card

Torvane Projects
Brett Lamonte
Managing Director
0491570156
brett@torvaneprojects.example.com.au

```html
<!DOCTYPE html>
<html lang="en">
<head>
<meta charset="utf-8">
<title>Torvane Projects – Business Card</title>
<link href="https://fonts.googleapis.com/css2?family=Jost:wght@400;500&family=Open+Sans:wght@400;600&display=swap" rel="stylesheet">
<style>
  :root {
    --stage: #1d1d1e;
    --card: #ffffff;
    --red: #e3202b;
    --grey-text: #55565a;
    --ink: #222326;
    --band-dark: #4a4b4e;
    --band-light: #a3a4a7;
  }
  * { box-sizing: border-box; margin: 0; padding: 0; }
  html, body {
    width: 1200px; height: 908px; overflow: hidden;
    background: var(--stage);
  }
  .stage {
    width: 1200px; height: 908px;
    display: flex; flex-direction: column;
    align-items: center; justify-content: center; gap: 56px;
  }
  .card {
    position: relative;
    width: 620px; height: 354px;
    background: var(--card);
    border-radius: 22px;
    overflow: hidden;
    box-shadow: 0 10px 28px rgba(0,0,0,.55);
  }
  .brand {
    font-family: "Jost", sans-serif;
    font-weight: 500;
    color: var(--grey-text);
    letter-spacing: .5px;
    white-space: nowrap;
  }
  /* back: blank notes area, name bottom-left */
  .card--back .brand {
    position: absolute; left: 34px; bottom: 30px;
    font-size: 30px;
  }
  /* front */
  .card--front .brand {
    position: absolute; left: 0; right: 0; top: 66px;
    text-align: center; font-size: 50px; line-height: 1;
  }
  .person {
    position: absolute; left: 0; right: 0; top: 146px;
    text-align: center;
    font-family: "Open Sans", sans-serif;
    line-height: 1.25;
  }
  .person__name {
    color: var(--red); font-size: 19px; font-weight: 600;
    letter-spacing: .4px; text-transform: uppercase;
  }
  .person__title { color: var(--ink); font-size: 14px; }
  .contact {
    position: absolute; left: 0; right: 0; top: 204px;
    font-family: "Open Sans", sans-serif; font-size: 16px; line-height: 1.3;
    color: var(--ink);
    display: flex; flex-direction: column; align-items: center; gap: 4px;
  }
  .contact__row { display: flex; align-items: center; gap: 8px; }
  .contact__icon { width: 16px; height: 16px; fill: var(--red); }
  .bands { position: absolute; left: 0; right: 0; bottom: 0; height: 48px; }
  .bands__red { position: absolute; top: 0; left: 0; right: 0; height: 5px; background: var(--red); }
  .bands__grey {
    position: absolute; top: 9px; bottom: 0; left: 0; right: 0;
    background: linear-gradient(100deg, var(--band-dark) 0%, var(--band-light) 40%, var(--band-dark) 100%);
  }
</style>
</head>
<body>
<main class="stage">
  <section class="card card--back" aria-label="Card back with notes area">
    <div class="brand">Torvane Projects</div>
  </section>

  <section class="card card--front" aria-label="Card front">
    <div class="brand">Torvane Projects</div>
    <div class="person">
      <div class="person__name">Brett Lamonte</div>
      <div class="person__title">Managing Director</div>
    </div>
    <div class="contact">
      <div class="contact__row">
        <svg class="contact__icon" viewBox="0 0 24 24" aria-hidden="true"><path d="M3 9c0-3 4-5 9-5s9 2 9 5v2h-5V9c-1-.6-2.4-1-4-1s-3 .4-4 1v2H3zM6 13h12l2 7H4z"/></svg>
        <span>0491570156</span>
      </div>
      <div class="contact__row">
        <svg class="contact__icon" viewBox="0 0 24 24" aria-hidden="true"><path d="M2 5h20v14H2zm2 2v.5l8 5.5 8-5.5V7z"/></svg>
        <span>brett@torvaneprojects.example.com.au</span>
      </div>
    </div>
    <div class="bands" aria-hidden="true">
      <div class="bands__red"></div>
      <div class="bands__grey"></div>
    </div>
  </section>
</main>
</body>
</html>
```